Wordpress Blog for Mobile Service Store

We need a website design for a genuine blog for related information to our mobile services we will provide in a future online shop (see a selection of products on our company page: http://www.corvexaplan.com/vas-catalogue/end-users.htm).

This blog is thought to engage our final clients to get in contact with us. We want to provide them useful information about our different product and give them various interaction possibilities, like feedback/comments, content rating, watch video/audio files, Social network Adding and subscriptions to our news feeds and Newsletter.

But at the same time, a way should be found that the blog doesn´t seem to be overloaded with information and that it will be very intuitive in use of all offered functionalities. A valuable extra would be developing of a design which is adaptable to future expansion and adaption of additional content, categories, boxes or adds of our products.
Updates

Hi everyone!

First of all, thanks a lot for taking part in our design project for our future Worldpress Blog Design for our mobile service store.

Up to now the Store looks like that (http://www.tundrashelfmart.com/es.html), but we thinking of major changes in design and a renaming of this store. It tooks us a time to define well the blog requirements, so it helps you a lot to check the short xcl., project brief and given examples beforehand to get a idea what we are looking for.

Based on the first submitted designs I want to give a short feedback:

• - The submitted designs up to now work with too dark/serious colors, please avoid black, where it isn´t necessary…visiting our blog should mean pleasure!
• Separate corporate & final clients design:
• The look and feel should be independent from our “Corvexa Plan” Company design, since we don’t want to make a direct reference to us within our new store. Our company itself, Corvexa Plan, has it’s own blog for their corporate news.
• - This blog is thought to connect with our end clients (someone like you and me) of our online store where we sell mobile apps (f.e. services for 1€ /month). So the design should be not that serious, but rather a touch more feminine and playful.
• - Not too many lists on main page! One section with reference to the most popular post is sufficient, a further reference to older post will be made at the bottom of a single post.
• - Out of our experience (more) pictures and visual elements catch more attention for a further reading  of a post (check out our given examples in the brief!), so we look for a more engaging post design, f.e. like the headlines of the new Quillstoat Blog.
• - Implement a sleek "advanced search bar", no need of a space-occupying "keyword cloud" - we want to avoid that our readers are overwhelmed with unnecessary  information.
So let´s get the best out of this!

We appreciate a lot your help!

Cheers, Henrike (marketing@corvexaplan.com)

Reason: Hi everyone, Since it´s holiday time here in Europe, might be that some of you are coming back from there right now...so we give you a week more time to submit your designs to our project. I will upload some more inside + pictures of our project to help to make it more easier for you what kind of design we are looking for. Thanks in advance for your dedication to our project =). Kind regards, Henrike =)

Target Market(s)

Our main target group are people who NOT owns a smart phone, but rather posses any kind of phone device, never mind how old, never mind the age, gender or profession.

By calling a land-line number everyone can have access to our Mobile Services. We offer services for professional use, but as well for leisure. Our clients have to pay for our service, so we want to transmit trust, proximity and professionalism.

The only criteria we have, is that our client has a minimum technical ability to subscribe himself to a service on our homepage and configure his account there.

Industry/Entity Type

Shop

Requirements
Must have
• Required design to the following screen- maximum width: 1400 px.
Design should be in a later stage adaptable to Worldpress Blog tool.
We need a design which visualize the main page and the single post.

!!! Please find attached an EXCEL FILE which lists all main components to implement in the design !!!

Look and feel (further inside)

Since we haven´t a final logo for our shop so far, neither a finished design we set any limits to your creativity (no restriction in color code). But in general we are looking for a modern, clean/tidy and fresh design which has an elegant, personable and playful touch.

We appreciate a lot innovative elements which distinguish from an ordinary blog design/structure. As it´s important that the site doesn´t appear too text heavy but rather has an engaging visual standout. Dynamic elements which open while making a mouse-over are, for example, nice features to cluster information so the page doesn´t seem to overloaded.

Concerning the content, find in this link in our existing company blog an example of news we used to publish: http://blog.corvexaplan.com/launch_tovidex. It´s important, that the font is not to small, but easy to read. That´s why a line spacing higher than 1.0 is wished for the blog post to meet this criteria.
Nice to have
• In the PDF Brief attached you find several URLs of Blogs which visualize in some part our main idea (please check them beforehand!)

Should not have
• We don´t look for an ordinary blog design.
Avoid too heavy text!

```html
<!DOCTYPE html>
<html lang="en">
<head>
<meta charset="utf-8">
<title>Corvexa Plan – Mobile Service Blog</title>
<link rel="stylesheet" href="https://fonts.googleapis.com/css2?family=Arimo:wght@400;700&family=Open+Sans:wght@400;600&display=swap">
<style>
  :root {
    --page-bg: #ffffff;
    --header-purple: #5b5283;
    --frame-purple: #4d4577;
    --footer-purple: #4b4373;
    --nav-top: #4f4875;
    --nav-bottom: #2b2645;
    --pill: #7a72a3;
    --lavender: #a49ccb;
    --lavender-light: #c9c3e6;
    --panel-head-top: #9a92c2;
    --panel-head-bottom: #4a4276;
    --ink: #2b2b2b;
    --title-ink: #2e2a52;
    --soft-grey: #e2e2e2;
    --line-grey: #6c6c6c;
    --star: #f2a516;
    --share-blue: #3b5a9a;
    --white: #ffffff;
  }
  * { box-sizing: border-box; margin: 0; padding: 0; }
  html, body { width: 960px; height: 1200px; overflow: hidden; background: var(--page-bg); }
  body { font-family: "Arimo", Arial, sans-serif; color: var(--ink); }
  .canvas { position: relative; width: 960px; height: 1200px; overflow: hidden; }
  .abs { position: absolute; }

  /* Header */
  .site-header { left: 20px; top: 0; width: 916px; height: 123px; background: linear-gradient(180deg, #625a8b, var(--header-purple)); }
  .brand { left: 32px; top: 30px; display: flex; align-items: center; gap: 14px; }
  .brand-dot { width: 38px; height: 38px; border-radius: 50%; background: var(--white); }
  .brand-name { font-family: "Arimo", Arial, sans-serif; font-size: 27px; color: var(--white); font-weight: 400; }
  .account-links { right: 30px; top: 14px; font-size: 12px; color: var(--white); display: flex; gap: 14px; }
  .header-field { left: 644px; font-size: 12px; color: var(--white); display: flex; align-items: center; }
  .header-field .label { width: 70px; }
  .header-field .colon { width: 11px; }
  .search-row { top: 48px; }
  .lang-row { top: 87px; }
  .search-input { width: 138px; height: 20px; border-radius: 10px; background: #4b4370; border: 1px solid #6e669a; }
  .go-btn { margin-left: 8px; width: 22px; height: 22px; border-radius: 50%; background: #4b4370; border: 1px solid #7a72a6; font-size: 9px; display: flex; align-items: center; justify-content: center; }
  .lang-select { width: 136px; height: 20px; border-radius: 4px; background: #4b4370; border: 1px solid #6e669a; color: #aaa4c8; font-size: 11px; padding-left: 12px; display: flex; align-items: center; justify-content: space-between; padding-right: 8px; }

  .main-nav { left: 11px; top: 123px; width: 933px; height: 42px; background: linear-gradient(180deg, var(--nav-top), var(--nav-bottom)); }
  .main-nav ul { list-style: none; position: relative; height: 100%; }
  .main-nav li { position: absolute; top: 10px; font-size: 16px; color: var(--white); }
  .main-nav li.active { top: 10px; left: 230px; width: 74px; height: 24px; border-radius: 6px; background: linear-gradient(180deg, #8e87b6, var(--pill)); text-align: center; line-height: 24px; border: 1px solid #9c95c4; }

  /* Frame */
  .content-frame { left: 20px; top: 165px; width: 916px; height: 870px; background: var(--frame-purple); }
  .content-area { left: 30px; top: 165px; width: 903px; height: 870px; background: var(--white); }

  /* Posts */
  .section-title { left: 43px; top: 187px; font-size: 22px; color: var(--title-ink); }
  .post-thumb { border: 1px solid #e4e4e4; box-shadow: 0 0 3px rgba(0,0,0,.12); }
  .post-body { font-family: "Open Sans", Arial, sans-serif; font-size: 11px; line-height: 17.4px; letter-spacing: .3px; color: var(--ink); width: 292px; }
  .post-meta { font-family: "Open Sans", Arial, sans-serif; font-size: 11px; color: var(--ink); text-align: center; width: 64px; }
  .stars { display: block; margin-top: 2px; }
  .comment-badge { width: 26px; height: 30px; }
  .share-row { display: flex; gap: 4px; }
  .share-btn { height: 15px; font-family: "Arimo", Arial, sans-serif; font-size: 8.5px; border: 1px solid #bcc4d6; background: #f3f5f9; color: #4a5b85; padding: 0 5px; line-height: 13px; border-radius: 2px; }
  .share-btn.primary { background: var(--share-blue); color: var(--white); border-color: var(--share-blue); font-weight: 700; padding: 0 10px; }
  .post-divider { left: 66px; width: 523px; border-top: 1px dotted #555; }

  .promo-banner { left: 38px; top: 849px; width: 567px; height: 170px; border: 4px solid #cfcfcf; background: linear-gradient(90deg, #e9ddd2 0%, #f6f2ee 45%, #ffffff 100%); }

  /* Sidebar */
  .video-player { left: 623px; top: 177px; width: 299px; height: 248px; background: #000; border: 1px solid #333; }
  .video-controls { position: absolute; left: 0; bottom: 0; width: 100%; height: 16px; background: linear-gradient(180deg, #e9e9e9, #bdbdbd); }
  .panel-head { left: 622px; width: 301px; height: 31px; border-radius: 10px 10px 0 0; background: linear-gradient(180deg, var(--panel-head-top), var(--panel-head-bottom)); color: var(--white); font-size: 22px; padding-left: 12px; line-height: 31px; box-shadow: 0 2px 3px rgba(0,0,0,.3); }
  .subscribe-list { left: 628px; top: 478px; width: 287px; }
  .subscribe-item { height: 38px; border-bottom: 1px dotted #333; display: flex; align-items: center; font-family: "Open Sans", Arial, sans-serif; font-size: 13px; color: #3d3868; }
  .subscribe-item .icon { width: 30px; height: 30px; border-radius: 50%; background: linear-gradient(180deg, #bdbdbd, #6b6b6b); margin: 0 17px 0 4px; flex: none; }
  .subscribe-item .icon.mail { background: linear-gradient(180deg, #f26b5b, #c6241a); }
  .email-input { width: 153px; height: 22px; border: 1px solid #aaa; }
  .email-btn { margin-left: 5px; height: 20px; padding: 0 8px; border-radius: 8px; background: linear-gradient(180deg, #9d96c4, #5f578c); color: var(--white); font-size: 11px; line-height: 20px; font-family: "Arimo", Arial, sans-serif; }

  .top-posts { left: 623px; top: 685px; width: 299px; }
  .top-post { height: 53px; background: var(--soft-grey); margin-bottom: 2px; display: flex; padding: 12px 8px 0 14px; font-size: 11.4px; line-height: 13.5px; color: #111; }
  .top-post svg { flex: none; margin: 1px 15px 0 0; }

  .older-posts { left: 623px; top: 942px; width: 299px; height: 77px; background: #000; border-radius: 0 0 8px 8px; padding: 8px 12px 0 20px; }
  .older-item { height: 29px; display: flex; align-items: center; font-family: "Open Sans", Arial, sans-serif; font-size: 13px; color: #d9d4f2; }
  .older-item + .older-item { border-top: 1px dotted #777; }
  .older-item .dot { width: 10px; height: 10px; border-radius: 50%; background: var(--lavender); margin-right: 22px; }

  /* Footer */
  .site-footer { left: 20px; top: 1035px; width: 916px; height: 165px; background: var(--footer-purple); }
  .footer-nav { left: 35px; top: 1058px; display: flex; font-size: 13px; color: #b2aad6; }
  .footer-nav span { margin-right: 42px; }
  .footer-nav .current { color: var(--lavender-light); }
  .footer-social { left: 38px; top: 1095px; display: flex; gap: 7px; }
  .footer-social span { width: 30px; height: 28px; border-radius: 7px; background: linear-gradient(180deg, #c9c9c9, #7e7e7e); }
  .newsletter-title { left: 449px; top: 1056px; font-size: 22px; color: #3a3362; }
  .nl-field { left: 450px; display: flex; align-items: center; font-size: 11px; color: var(--white); }
  .nl-field .label { width: 70px; }
  .nl-field .colon { width: 9px; }
  .nl-input { width: 210px; height: 20px; background: #433b68; border: 1px solid #2e2850; }
  .submit-btn { left: 755px; top: 1129px; width: 77px; height: 22px; border-radius: 10px; background: linear-gradient(180deg, #cfcaf0, #a8a1d2); color: #25204a; font-size: 13px; text-align: center; line-height: 22px; }
</style>
</head>
<body>
<div class="canvas">

  <header class="site-header abs">
    <div class="brand abs">
      <span class="brand-dot"></span>
      <span class="brand-name">Corvexa Plan</span>
    </div>
    <div class="account-links abs"><span>Sign in</span><span>Create Account</span></div>
  </header>
  <div class="header-field search-row abs"><span class="label">Search</span><span class="colon">:</span><span class="search-input"></span><span class="go-btn">GO</span></div>
  <div class="header-field lang-row abs"><span class="label">Languages</span><span class="colon">:</span><span class="lang-select">English <svg width="10" height="8"><polygon points="0,0 10,0 5,8" fill="#e0dcf2"/></svg></span></div>

  <nav class="main-nav abs">
    <ul>
      <li class="active">Home</li>
      <li style="left:355px">Store</li>
      <li style="left:459px">Feedback</li>
      <li style="left:593px">Contact</li>
    </ul>
  </nav>

  <div class="content-frame abs"></div>
  <main class="content-area abs"></main>

  <h2 class="section-title abs" style="font-weight:400">Most Popular Posts</h2>

  <!-- Post 1 -->
  <div class="post-thumb abs" style="left:45px;top:220px;width:216px;height:205px;background:linear-gradient(135deg,#f4f4f4,#3a3a3a 40%,#2a8fb0 70%,#e8f3f6);" role="img" aria-label="Two compact keypad mobile phones, one black and one turquoise"></div>
  <div class="post-meta abs" style="left:474px;top:199px">Comments
    <svg class="stars" width="64" height="14" viewBox="0 0 80 16"><g fill="var(--star)" stroke="#c47f06" stroke-width=".6"><polygon id="st" points="8,0 10.4,5.3 16,5.8 11.7,9.5 13,15 8,12 3,15 4.3,9.5 0,5.8 5.6,5.3"/><use href="#st" x="16"/><use href="#st" x="32"/><use href="#st" x="48"/><use href="#st" x="64"/></g></svg>
  </div>
  <svg class="comment-badge abs" style="left:558px;top:200px" viewBox="0 0 26 30"><path d="M0 0H26V22H14L10 30V22H0Z" fill="#8d8d8d"/><text x="13" y="15" font-size="10" text-anchor="middle" fill="#fff" font-family="Arimo, Arial, sans-serif">23</text></svg>
  <p class="post-body abs" style="left:283px;top:253px">It is a long established fact that a reader will be distracted by the readable content of a page when looking at its layout. The point of using Lorem Ipsum is that it has a more-or-less normal distribution of letters, as opposed to using 'Content here, content here', making it look like readable English. Many desktop publishing</p>
  <div class="share-row abs" style="left:408px;top:397px"><span class="share-btn">Chirpline</span><span class="share-btn">Like</span><span class="share-btn primary">Share</span></div>
  <div class="post-divider abs" style="top:434px"></div>

  <!-- Post 2 -->
  <div class="post-thumb abs" style="left:45px;top:460px;width:216px;height:205px;background:linear-gradient(135deg,#ffffff,#1b1b1b 35%,#5d7a9b 60%,#f2f2f2);" role="img" aria-label="Three touchscreen smartphones standing side by side"></div>
  <div class="post-meta abs" style="left:474px;top:439px">Comments
    <svg class="stars" width="64" height="14" viewBox="0 0 80 16"><g fill="var(--star)" stroke="#c47f06" stroke-width=".6"><use href="#st"/><use href="#st" x="16"/><use href="#st" x="32"/><use href="#st" x="48"/><use href="#st" x="64"/></g></svg>
  </div>
  <svg class="comment-badge abs" style="left:558px;top:440px" viewBox="0 0 26 30"><path d="M0 0H26V22H14L10 30V22H0Z" fill="#8d8d8d"/><text x="13" y="15" font-size="10" text-anchor="middle" fill="#fff" font-family="Arimo, Arial, sans-serif">23</text></svg>
  <p class="post-body abs" style="left:283px;top:493px">It is a long established fact that a reader will be distracted by the readable content of a page when looking at its layout. The point of using Lorem Ipsum is that it has a more-or-less normal distribution of letters, as opposed to using 'Content here, content here', making it look like readable English. Many desktop publishing</p>
  <div class="share-row abs" style="left:409px;top:637px"><span class="share-btn">Chirpline</span><span class="share-btn">Like</span><span class="share-btn primary">Share</span></div>
  <div class="post-divider abs" style="top:673px"></div>

  <!-- Post 3 -->
  <div class="post-thumb abs" style="left:45px;top:699px;width:216px;height:131px;background:linear-gradient(160deg,#c9d9e8,#6f8fb5 35%,#e6a84a 55%,#2a2a2a 80%,#f4f4f4);" role="img" aria-label="Colourful app icons spilling out of a smartphone screen"></div>
  <div class="post-meta abs" style="left:474px;top:678px">Comments
    <svg class="stars" width="64" height="14" viewBox="0 0 80 16"><g fill="var(--star)" stroke="#c47f06" stroke-width=".6"><use href="#st"/><use href="#st" x="16"/><use href="#st" x="32"/><use href="#st" x="48"/><use href="#st" x="64"/></g></svg>
  </div>
  <svg class="comment-badge abs" style="left:558px;top:679px" viewBox="0 0 26 30"><path d="M0 0H26V22H14L10 30V22H0Z" fill="#8d8d8d"/><text x="13" y="15" font-size="10" text-anchor="middle" fill="#fff" font-family="Arimo, Arial, sans-serif">23</text></svg>
  <p class="post-body abs" style="left:283px;top:733px">It is a long established fact that a reader will be distracted by the readable content of a page when looking at its layout. The point of using Lorem Ipsum is that it has a more-or-less normal distribution</p>
  <div class="share-row abs" style="left:417px;top:812px"><span class="share-btn">Chirpline</span><span class="share-btn">Like</span><span class="share-btn primary">Share</span></div>

  <div class="promo-banner abs" role="img" aria-label="Advertisement for Mindvault, Empowering Innovation: a woman holding a smartphone next to a brain illustration"></div>

  <!-- Sidebar -->
  <div class="video-player abs" role="img" aria-label="Embedded video player">
    <svg class="abs" style="left:124px;top:98px" width="50" height="34" viewBox="0 0 50 34"><rect x="1" y="1" width="48" height="32" rx="6" fill="#6a6a6a" stroke="#aaa"/><polygon points="19,9 33,17 19,25" fill="#111"/></svg>
    <div class="video-controls"></div>
  </div>

  <h3 class="panel-head abs" style="top:442px;font-weight:400">Subscribe</h3>
  <ul class="subscribe-list abs" style="list-style:none">
    <li class="subscribe-item"><span class="icon mail"></span><span class="email-input"></span><span class="email-btn">Get E-mails</span></li>
    <li class="subscribe-item"><span class="icon"></span>RSS Feed</li>
    <li class="subscribe-item"><span class="icon"></span>Find us on Friendspace</li>
    <li class="subscribe-item"><span class="icon"></span>Follow us on Chirpline</li>
  </ul>

  <h3 class="panel-head abs" style="top:653px;font-weight:400;padding-left:22px">Top Posts</h3>
  <ul class="top-posts abs" style="list-style:none">
    <li class="top-post"><svg width="16" height="12" viewBox="0 0 16 12"><path d="M1 0L7 6L1 12H4L10 6L4 0ZM7 0L13 6L7 12H10L16 6L10 0Z" fill="#4a4276"/></svg><span>How we almost didn't raise $800K in the orst investment market in years</span></li>
    <li class="top-post"><svg width="16" height="12" viewBox="0 0 16 12"><path d="M1 0L7 6L1 12H4L10 6L4 0ZM7 0L13 6L7 12H10L16 6L10 0Z" fill="#4a4276"/></svg><span>The Science of Customer Service: Data Proves Faster Response Means Happier Customers</span></li>
    <li class="top-post"><svg width="16" height="12" viewBox="0 0 16 12"><path d="M1 0L7 6L1 12H4L10 6L4 0ZM7 0L13 6L7 12H10L16 6L10 0Z" fill="#4a4276"/></svg><span>Case Study: Profilo uses Voicebay Full Service to measure customer happiness</span></li>
    <li class="top-post" style="height:56px;padding-top:14px"><svg width="16" height="12" viewBox="0 0 16 12"><path d="M1 0L7 6L1 12H4L10 6L4 0ZM7 0L13 6L7 12H10L16 6L10 0Z" fill="#4a4276"/></svg><span>Scheduled Downtime This Saturday</span></li>
  </ul>

  <h3 class="panel-head abs" style="top:912px;font-weight:400;padding-left:20px">Older Posts</h3>
  <ul class="older-posts abs" style="list-style:none">
    <li class="older-item"><span class="dot"></span>February 2009</li>
    <li class="older-item"><span class="dot"></span>January 2009</li>
  </ul>

  <!-- Footer -->
  <footer class="site-footer abs"></footer>
  <div class="footer-nav abs"><span class="current">Home</span><span>Store</span><span>Feedback</span><span>Contact</span></div>
  <div class="footer-social abs"><span></span><span></span><span></span></div>
  <h3 class="newsletter-title abs" style="font-weight:400">News Letter Subscribe</h3>
  <div class="nl-field abs" style="top:1104px"><span class="label">Name</span><span class="colon">:</span><span class="nl-input"></span></div>
  <div class="nl-field abs" style="top:1132px"><span class="label">Email</span><span class="colon">:</span><span class="nl-input"></span></div>
  <div class="submit-btn abs">Submit</div>

</div>
</body>
</html>
```